Autodetailing namecard design: Rose Gold Lettering on Black Matt

This is a namecard design project
requiring two-sided design
Base Color of Namecard: black matt

On front:
Company name,
"Lumina Finishes 14 Cendana"
Subtext: Auto Detailing Studio

Name of card holder: Marcus Oyelaran
Phone Number: +6011-4837-5062
address: 14, Jalan Cendana 5/3Taman Seri Cendana, 81400 Johor Bahru, Johor, Malaysia

Back:
Our Services
High Gloss Car Paint Protection
Custom Color Modification and Styling
Anti-Chip Glass Protection Film
Heat Rejection Glass Tinting

Target Market(s)

Autodetailing for highend cars

Contact Information for Business Card

as mentioned in project details

Colors

Designer to choose colors to be used in the design.

Requirements
Must have
• The main value-add to this project is the design of a logo suited for our purpose and name, and the inclusion of business card details into the card design

```html
<!DOCTYPE html>
<html lang="en">
<head>
<meta charset="utf-8">
<title>Lumina Finishes 14 Cendana — Business Card</title>
<link rel="stylesheet" href="https://fonts.googleapis.com/css2?family=Lato:wght@400;700&family=Roboto+Condensed:wght@400&display=swap">
<style>
  :root {
    --backdrop: #ece8e5;
    --card-matte: #1b1a1a;
    --rose: #d2957e;
    --rose-light: #e2ab9b;
    --rose-deep: #c47e6b;
    --ink-on-matte: #d9d4d1;
    --divider: #6a6360;
    --on-rose: #ffffff;
  }
  * { margin: 0; padding: 0; box-sizing: border-box; }
  html, body {
    width: 1200px; height: 900px; overflow: hidden;
    background: var(--backdrop);
  }
  .canvas { position: relative; width: 1200px; height: 900px; }

  .card {
    position: absolute;
    width: 556px; height: 343px;
    box-shadow: 0 3px 8px rgba(0,0,0,0.18);
  }
  .card--front { left: 330px; top: 90px; background: var(--card-matte); }
  .card--back {
    left: 330px; top: 469px; width: 559px;
    background: radial-gradient(ellipse 60% 75% at 50% 35%, var(--rose-light), var(--rose-deep));
  }

  .brand-name, .brand-sub {
    position: absolute;
    font-family: "Lato", sans-serif;
    text-transform: uppercase;
    text-align: center;
    white-space: nowrap;
  }
  .brand-name { font-weight: 700; line-height: 1.2; letter-spacing: 1px; }
  .brand-sub { font-weight: 400; line-height: 1; }

  .card--front .brand-name {
    left: 32px; top: 120px; width: 234px;
    font-size: 23px; color: var(--rose);
  }
  .card--front .brand-sub {
    left: 32px; top: 219px; width: 234px;
    font-size: 16px; color: var(--rose);
    padding-bottom: 6px; border-bottom: 2px solid var(--rose);
  }

  .card--back .brand-name {
    left: 130px; top: 98px; width: 300px;
    font-size: 30px; color: var(--on-rose);
  }
  .card--back .brand-sub {
    left: 158px; top: 206px; width: 242px;
    font-size: 19px; color: var(--on-rose);
    padding-bottom: 6px; border-bottom: 3px solid var(--on-rose);
  }

  .divider {
    position: absolute; left: 289px; top: 108px;
    width: 1px; height: 127px; background: var(--divider);
  }
  .holder {
    position: absolute; left: 315px; top: 101px;
    font-family: "Lato", sans-serif;
  }
  .holder-name {
    font-size: 21px; font-weight: 400; color: var(--rose);
    text-transform: uppercase; line-height: 26px; white-space: nowrap;
  }
  .holder-phone { font-size: 16px; color: var(--ink-on-matte); line-height: 20px; }
  .holder-address {
    margin-top: 13px; font-size: 16px; color: var(--ink-on-matte);
    line-height: 20.3px; font-style: normal;
  }

  .services-rule {
    position: absolute; left: 46px; top: 258px;
    width: 466px; height: 1px; background: rgba(255,255,255,0.7);
  }
  .services {
    position: absolute; left: 0; top: 271px; width: 559px;
    list-style: none; text-align: center;
    font-family: "Roboto Condensed", sans-serif;
    font-size: 16px; line-height: 21px; color: var(--on-rose);
  }
</style>
</head>
<body>
<main class="canvas">
  <section class="card card--front" aria-label="Card front">
    <p class="brand-name">Lumina Finishes<br>14 Cendana</p>
    <p class="brand-sub">Auto Detailing Studio</p>
    <div class="divider"></div>
    <div class="holder">
      <p class="holder-name">Marcus Oyelaran</p>
      <p class="holder-phone">+6011-4837-5062</p>
      <address class="holder-address">
        14, Jalan Cendana<br>
        5/3Taman Seri Cendana,<br>
        81400 Johor Bahru<br>
        Johor, Malaysia
      </address>
    </div>
  </section>

  <section class="card card--back" aria-label="Card back">
    <p class="brand-name">Lumina Finishes<br>14 Cendana</p>
    <p class="brand-sub">Auto Detailing Studio</p>
    <div class="services-rule"></div>
    <ul class="services">
      <li>High Gloss Car Paint Protection | Custom Color Modification and Styling</li>
      <li>Anti-Chip Glass Protection Film &nbsp;| Heat Rejection Glass Tinting</li>
    </ul>
  </section>
</main>
</body>
</html>
```